International Sex Coach needs a Book Cover in less than 3 days

I need a cover design for my book coming out next week titled "The Open Map of Desire". The book explores the origins of our cultural ideas about sexuality and taboo and is interwoven with personal memoir.
The reader must feel that they are being pulled into an intimate sexual story, but also a deeper understanding of sex itself. Like they are jumping into bed with me, you might say. I would like the title to take up the majority of the space over an image of 3D, very real bed sheets, but I am open to your ideas. I haven't purchased any images yet, but there are a few below I was drawn to.
In its essence, this book is designed to reeducate the reader about sexuality and open them up to a new paradigm of sexual wellness.
The author name is Marisa Tolven. Page must also include the phrase: a revolutionary new approach to sexuality, relationship and love.
Size 6" x 9" (15.24 x 22.86 cm)
Thanks!
Updates

Target Market(s)

Sexually active men and women.

Industry/Entity Type

Wellness

Font styles to use
Serif

```html
<!DOCTYPE html>
<html lang="en">
<head>
<meta charset="utf-8">
<title>The Open Map of Desire — Book Cover</title>
<link rel="stylesheet" href="https://fonts.googleapis.com/css2?family=Marcellus&family=Alegreya:wght@400&display=swap">
<style>
  :root {
    --ink: #1d1a19;
    --satin-light: #fbfaf6;
    --satin-mid: #ecebe5;
    --satin-shadow: #d8d7d0;
    --skin-light: #f4c9a6;
    --skin-mid: #e2a27a;
    --hair-gold: #d9a45a;
    --hair-deep: #9a6a3a;
  }
  html, body {
    margin: 0;
    padding: 0;
    width: 823px;
    height: 1200px;
    overflow: hidden;
    background: var(--satin-light);
  }
  .cover {
    position: relative;
    width: 823px;
    height: 1200px;
    overflow: hidden;
  }
  .sheet-backdrop {
    position: absolute;
    inset: 0;
    background:
      radial-gradient(ellipse at 70% 30%, var(--satin-light) 0%, transparent 55%),
      radial-gradient(ellipse at 80% 85%, var(--satin-shadow) 0%, transparent 45%),
      linear-gradient(160deg, var(--satin-light) 0%, var(--satin-mid) 45%, var(--satin-light) 70%, var(--satin-shadow) 100%);
  }
  .portrait-wedge {
    position: absolute;
    left: 0;
    top: 0;
    width: 823px;
    height: 1200px;
  }
  .title {
    position: absolute;
    right: 67px;
    top: 78px;
    margin: 0;
    text-align: right;
    font-family: "Marcellus", serif;
    font-weight: 400;
    color: var(--ink);
    line-height: 1;
  }
  .title-line-small {
    display: block;
    font-size: 60px;
    letter-spacing: 1px;
  }
  .title-line-large {
    display: block;
    font-size: 98px;
    margin-top: 2px;
    letter-spacing: 1px;
  }
  .tagline {
    position: absolute;
    right: 46px;
    top: 850px;
    margin: 0;
    text-align: right;
    font-family: "Alegreya", serif;
    font-size: 37px;
    line-height: 48px;
    color: var(--ink);
  }
  .author {
    position: absolute;
    right: 48px;
    top: 1104px;
    margin: 0;
    font-family: "Alegreya", serif;
    font-size: 20px;
    color: var(--ink);
  }
</style>
</head>
<body>
<main class="cover">
  <div class="sheet-backdrop" role="img" aria-label="Photograph of rumpled white satin bed sheets"></div>

  <svg class="portrait-wedge" viewBox="0 0 823 1200" role="img" aria-label="Photograph of a blonde woman looking down, framed in a rightward-pointing triangle">
    <defs>
      <linearGradient id="wedge-tone" x1="0" y1="0" x2="1" y2="1">
        <stop offset="0" stop-color="var(--hair-deep)"/>
        <stop offset="0.25" stop-color="var(--hair-gold)"/>
        <stop offset="0.55" stop-color="var(--skin-light)"/>
        <stop offset="1" stop-color="var(--skin-mid)"/>
      </linearGradient>
    </defs>
    <polygon points="0,152 746,623 0,1081" fill="url(#wedge-tone)"/>
  </svg>

  <h1 class="title">
    <span class="title-line-small">THE OPEN MAP</span>
    <span class="title-line-large">OF DESIRE</span>
  </h1>

  <p class="tagline">A revolutionary<br>new approach<br>to sexuality,<br>relationship and love.</p>

  <p class="author">Marisa Tolven</p>
</main>
</body>
</html>
```